National online rug retailer needs a home page design

See the LoomNest logo and create a home page design around that color theme. Details are spelled out in word document uploaded below.
Updates

Apparently this website did not take my attachement showing the logo and basic requirements.  If you would send me your email address, I will send you the attachment directly.
Best regards,
Ned Carver
ncarver@qwplex.com

Target Market(s)

The target market is home owners 25 to 75 years old with combined incomes over $100,000 per year.

Industry/Entity Type

Online

Requirements
Must have
• Lots of white space with black letters and creative use of red and possibly one other color. Would like a compelling call to action button.

```html
<!DOCTYPE html>
<html lang="en">
<head>
<meta charset="utf-8">
<title>LoomNest — Home</title>
<link href="https://fonts.googleapis.com/css2?family=Open+Sans:wght@400;600;700&display=swap" rel="stylesheet">
<style>
  :root {
    --red: #e21b1b;
    --ink: #222;
    --text: #444;
    --muted: #777;
    --line: #dcdcdc;
    --panel: #efefef;
    --nav: #ececec;
    --dark: #2b2b2b;
    --white: #fff;
  }
  * { box-sizing: border-box; margin: 0; padding: 0; }
  html, body { width: 833px; height: 1200px; overflow: hidden; background: var(--white); }
  body { position: relative; font-family: "Open Sans", Arial, sans-serif; color: var(--text); }
  a { color: inherit; text-decoration: none; }
  .abs { position: absolute; }

  /* header */
  .brand { left: 83px; top: 14px; display: flex; align-items: center; gap: 8px; }
  .brand-mark { width: 30px; height: 30px; background: var(--red); }
  .brand-name { font-size: 30px; font-weight: 600; color: var(--red); letter-spacing: -0.5px; }
  .brand-tag { left: 154px; top: 61px; font-size: 10px; color: var(--muted); }
  .top-links { right: 83px; top: 11px; display: flex; gap: 11px; font-size: 8.5px; color: var(--text); align-items: center; }
  .top-links .sel { font-weight: 600; color: var(--ink); }
  .cart { left: 644px; top: 31px; display: flex; align-items: center; gap: 6px; font-size: 10px; color: var(--ink); }
  .cart .empty { color: var(--muted); font-size: 9.5px; }
  .search { left: 502px; top: 56px; width: 248px; height: 29px; border: 1px solid var(--line); font-size: 9px; color: #aaa; padding: 9px 8px; }
  .search svg { position: absolute; right: 8px; top: 7px; }

  /* nav */
  .nav { left: 83px; top: 100px; width: 667px; height: 38px; background: var(--nav); border-bottom: 4px solid var(--red); display: flex; align-items: center; font-size: 11px; color: var(--ink); }
  .nav a { padding: 0 11.5px; line-height: 34px; }
  .nav .active { background: var(--red); color: var(--white); font-weight: 700; padding: 0 10px; }
  .plus { width: 17px; height: 17px; background: var(--red); display: inline-block; position: relative; }
  .plus::before, .plus::after { content: ""; position: absolute; background: var(--white); }
  .plus::before { left: 3px; right: 3px; top: 7.5px; height: 2px; }
  .plus::after { top: 3px; bottom: 3px; left: 7.5px; width: 2px; }
  .nav .plus { position: absolute; right: 13px; top: 8px; }

  /* hero tiles */
  .tile { width: 326px; height: 186px; overflow: hidden; }
  .tile .photo { width: 100%; height: 100%; }
  .tile .caption { position: absolute; left: 0; right: 0; bottom: 0; height: 34px; background: rgba(30,30,30,.85); color: var(--white); font-size: 26px; font-weight: 700; padding-left: 36px; line-height: 34px; }
  .tile .caption svg { position: absolute; right: 20px; top: 7px; }

  /* featured */
  .section-head { left: 83px; top: 566px; width: 499px; height: 38px; background: var(--nav); border-bottom: 4px solid var(--red); font-size: 16px; color: var(--ink); padding: 10px 10px; }
  .section-head .plus { position: absolute; right: 10px; top: 9px; }
  .card { width: 159px; height: 158px; border: 1px solid var(--line); padding: 6px; }
  .card .photo { width: 146px; height: 90px; }
  .card p { font-size: 8.3px; line-height: 14px; color: var(--text); margin-top: 7px; }
  .buy { display: flex; gap: 3px; margin-top: 5px; font-size: 10px; font-weight: 600; color: var(--white); }
  .buy .price { background: var(--red); padding: 1px 4px; }
  .buy .add { background: var(--dark); padding: 1px 5px; font-weight: 400; }

  .categories { left: 591px; top: 566px; width: 159px; height: 209px; border: 1px solid var(--line); }
  .categories h2 { font-size: 16px; font-weight: 400; color: var(--ink); background: var(--nav); padding: 5px 10px; height: 29px; }
  .categories li { list-style: none; font-size: 9px; color: var(--ink); height: 25.3px; line-height: 25px; padding-left: 24px; border-bottom: 1px solid #f2f2f2; position: relative; }
  .categories li::before { content: ""; position: absolute; left: 11px; top: 11px; width: 4px; height: 4px; border-radius: 50%; background: #ccc; }
  .also { left: 592px; top: 790px; width: 159px; height: 158px; border: 1px solid var(--line); padding: 6px; }
  .also .photo { height: 145px; position: relative; }
  .also .label { position: absolute; left: 0; right: 0; bottom: 0; height: 24px; background: rgba(30,30,30,.85); color: var(--white); font-size: 10px; text-align: center; line-height: 24px; }

  /* footer */
  .footer { left: 83px; top: 967px; width: 667px; height: 233px; background: var(--panel); }
  .footer h3 { font-size: 11px; font-weight: 400; color: var(--ink); margin-bottom: 8px; }
  .footer ul { list-style: none; font-size: 8.3px; color: var(--text); line-height: 16px; }
  .fcol { position: absolute; top: 17px; }
  .pay { display: flex; gap: 4px; margin-top: 4px; align-items: center; }
  .pay span { width: 19px; height: 13px; background: #ccc; border: 1px solid #bbb; }
  .pay .later { width: auto; height: auto; background: none; border: 0; font-size: 13px; color: #1c3f8c; margin-left: 4px; }
  .badges { display: flex; gap: 6px; margin-top: 14px; align-items: center; }
  .badges .round { width: 30px; height: 30px; border-radius: 50%; background: #d6c57a; }
  .badges .sq { width: 36px; height: 20px; background: #cfcfcf; }
  .legal { position: absolute; left: 0; right: 0; bottom: 0; height: 30px; border-top: 1px solid #e2e2e2; font-size: 8.3px; color: var(--text); padding: 9px 10px; display: flex; justify-content: space-between; }
</style>
</head>
<body>

<header>
  <div class="abs brand"><span class="brand-mark"></span><span class="brand-name">LoomNest.com</span></div>
  <div class="abs brand-tag">for domestic and heirloom values</div>
  <nav class="abs top-links">
    <a href="#">My Account</a><a href="#">My Wishlist</a><a href="#">My Cart</a><a href="#">Chech Out</a><a href="#">Login</a>
    <span class="sel">En ⌄</span><span class="sel">$ ⌄</span>
    <svg width="9" height="10" viewBox="0 0 9 10"><rect x="0" y="4" width="9" height="6" fill="#444"/><path d="M2 4V2.5a2.5 2.5 0 0 1 5 0V4" stroke="#444" stroke-width="1.3" fill="none"/></svg>
  </nav>
  <div class="abs cart">
    <svg width="18" height="15" viewBox="0 0 18 15"><path d="M0 1h3l2 9h10l2-7H4.5" stroke="#333" stroke-width="1.6" fill="none"/><circle cx="6" cy="13" r="1.5" fill="#333"/><circle cx="14" cy="13" r="1.5" fill="#333"/></svg>
    <b style="font-weight:600">Cart</b><span class="empty">( empty )</span><span class="empty">&nbsp;⌄</span>
  </div>
  <div class="abs search">Enter keyword or items...
    <svg width="13" height="13" viewBox="0 0 13 13"><circle cx="5.5" cy="5.5" r="4" stroke="#bbb" stroke-width="1.6" fill="none"/><path d="M8.5 8.5l3.5 3.5" stroke="#bbb" stroke-width="1.8"/></svg>
  </div>
</header>

<nav class="abs nav">
  <a class="active" href="#">Home</a><a href="#">Selection Guide</a><a href="#">Rug Care</a><a href="#">FAQ</a><a href="#">Return Policy</a><a href="#">Free Shipping</a><a href="#">Clearance Rug</a><a href="#">Contact Us</a>
  <span class="plus"></span>
</nav>

<section>
  <a class="abs tile" style="left:83px;top:151px" href="#">
    <div class="photo" role="img" aria-label="Bright modern living room with white sofas and a patterned rug" style="background:linear-gradient(180deg,#d9d6d1,#a49c92 60%,#6e665e)"></div>
    <div class="caption">Modern Rugs<svg width="14" height="20" viewBox="0 0 14 20"><path d="M2 2l9 8-9 8" stroke="#fff" stroke-width="3" fill="none"/></svg></div>
  </a>
  <a class="abs tile" style="left:424px;top:151px" href="#">
    <div class="photo" role="img" aria-label="White living room with red cushions and a zebra-striped rug" style="background:linear-gradient(180deg,#e6e2de,#b9b3ad 55%,#4a4644)"></div>
    <div class="caption">Traditional<svg width="14" height="20" viewBox="0 0 14 20"><path d="M2 2l9 8-9 8" stroke="#fff" stroke-width="3" fill="none"/></svg></div>
  </a>
  <a class="abs tile" style="left:83px;top:351px" href="#">
    <div class="photo" role="img" aria-label="Open-plan room with wood ceiling, cream sofa and patterned rug" style="background:linear-gradient(180deg,#6b4b33,#b9a58e 50%,#8a7660)"></div>
    <div class="caption">Transitional<svg width="14" height="20" viewBox="0 0 14 20"><path d="M2 2l9 8-9 8" stroke="#fff" stroke-width="3" fill="none"/></svg></div>
  </a>
  <a class="abs tile" style="left:424px;top:351px" href="#">
    <div class="photo" role="img" aria-label="Shaggy brown rug before a fireplace with a leather armchair" style="background:linear-gradient(180deg,#4b3526,#8e6b57 45%,#a88877)"></div>
    <div class="caption">Casual<svg width="14" height="20" viewBox="0 0 14 20"><path d="M2 2l9 8-9 8" stroke="#fff" stroke-width="3" fill="none"/></svg></div>
  </a>
</section>

<section>
  <h2 class="abs section-head" style="font-weight:400">Featured Products<span class="plus"></span></h2>

  <div class="abs card" style="left:83px;top:617px">
    <div class="photo" role="img" aria-label="Black rug with colourful circle pattern" style="background:linear-gradient(135deg,#3a2a1e,#5b4533)"></div>
    <p>Lorem ipsum dolor sit amet consec teture adipisicing.</p>
    <div class="buy"><span class="price">$ 49.68</span><span class="add">Add to Cart</span></div>
  </div>
  <div class="abs card" style="left:252px;top:617px">
    <div class="photo" role="img" aria-label="Stacked red, green and grey patterned rugs" style="background:linear-gradient(135deg,#6c5b48,#b4532e 50%,#8b8a3c)"></div>
    <p>Lorem ipsum dolor sit amet consec teture adipisicing.</p>
    <div class="buy"><span class="price">$ 49.68</span><span class="add">Add to Cart</span></div>
  </div>
  <div class="abs card" style="left:422px;top:617px">
    <div class="photo" role="img" aria-label="Shag rug in red, orange and yellow squares" style="background:linear-gradient(135deg,#c6271a,#e4892a 50%,#e8c133)"></div>
    <p>Lorem ipsum dolor sit amet consec teture adipisicing.</p>
    <div class="buy"><span class="price">$ 49.68</span><span class="add">Add to Cart</span></div>
  </div>
  <div class="abs card" style="left:83px;top:790px">
    <div class="photo" role="img" aria-label="Black rug with grey and white arc pattern" style="background:linear-gradient(135deg,#222,#6e6e6e 55%,#1a1a1a)"></div>
    <p>Lorem ipsum dolor sit amet consec teture adipisicing.</p>
    <div class="buy"><span class="price">$ 49.68</span><span class="add">Add to Cart</span></div>
  </div>
  <div class="abs card" style="left:252px;top:790px">
    <div class="photo" role="img" aria-label="Traditional red medallion rug" style="background:linear-gradient(135deg,#efeae6,#8a2a1f 40%,#6a1f17 70%,#efeae6)"></div>
    <p>Lorem ipsum dolor sit amet consec teture adipisicing.</p>
    <div class="buy"><span class="price">$ 49.68</span><span class="add">Add to Cart</span></div>
  </div>
  <div class="abs card" style="left:422px;top:790px">
    <div class="photo" role="img" aria-label="Pale sage rugs with ornate tone-on-tone pattern" style="background:linear-gradient(135deg,#d9d8c8,#b8baa2 50%,#cfcdb8)"></div>
    <p>Lorem ipsum dolor sit amet consec teture adipisicing.</p>
    <div class="buy"><span class="price">$ 49.68</span><span class="add">Add to Cart</span></div>
  </div>

  <aside class="abs categories">
    <h2>Categories</h2>
    <ul>
      <li>RUG THEME</li><li>COLOR WAY</li><li>SIZE</li><li>SHAPE</li><li>FIBER CONTENT</li><li>MFGR. BRAND</li><li>MFGR.COLLECTION</li>
    </ul>
  </aside>

  <div class="abs also">
    <div class="photo" role="img" aria-label="Bare feet stepping on a soft blue shag rug" style="background:linear-gradient(180deg,#cfd3da,#8b97ac 55%,#5b6a85)">
      <div class="label">YOU MAY ALSO LIKE</div>
    </div>
  </div>
</section>

<footer class="abs footer">
  <div class="fcol" style="left:11px">
    <h3>Customer Services</h3>
    <ul><li>Shipping</li><li>Return Policy</li><li>Privacy Policy</li><li>Ordering &amp; Delivery Checklist</li><li>Terms of Use</li><li>Terms of Sale</li><li>Contact Us</li><li>Environmental Policy</li></ul>
  </div>
  <div class="fcol" style="left:167px">
    <h3>Resources</h3>
    <ul><li>Product Articles</li><li>Learning Center</li><li>Help</li><li>Refer A Friend</li><li>LoomNest Blog</li><li>Room Scene Viewer</li><li>Site Map</li><li>FAQ</li><li>Customer Testimonials</li><li>Photo Gallery</li></ul>
  </div>
  <div class="fcol" style="left:311px">
    <h3>Corporate Info</h3>
    <ul><li>About LoomNest.com</li><li>Careers</li><li>Affiliates</li></ul>
  </div>
  <div class="fcol" style="left:447px">
    <h3>Payment &amp; Shipping</h3>
    <div class="pay"><span></span><span></span><span></span><span></span><span></span><span class="later">DeferPay</span></div>
    <div class="badges"><span class="round"></span><span class="round"></span><span class="sq"></span><span class="sq"></span><span class="sq"></span></div>
  </div>
  <div class="legal"><span>© 2013 LoomNest All Rights Reserved.</span><span>Terms &amp; Condition &nbsp;| &nbsp;Privacy Policy</span></div>
</footer>

</body>
</html>
```